New company business cards with new company logo

We need a new business card designed as we have a new company logo and are going for a more 'flat design' look. Our company name is Veloristat and we are a global data focused Clinical Research Organisation. We'd ideally like one side with room for the individuals contact details, our full logo and our services - and one side which is quite plain, for example perhaps using the green triangular image attached with just the white 'V' in the center (also attached).

Industry/Entity Type

Business

Requirements
Must have
• Our main colour: #42b5a9
Please make text dark grey: #373737

```html
<!DOCTYPE html>
<html lang="en">
<head>
<meta charset="utf-8">
<title>Veloristat business cards</title>
<link href="https://fonts.googleapis.com/css2?family=Open+Sans:wght@400&family=Lora:wght@400&display=swap" rel="stylesheet">
<style>
  :root {
    --brand: #42b5a9;
    --brand-faint: #e3f3f1;
    --text: #373737;
    --card: #ffffff;
    --backdrop: #1f1e1f;
    --rule: #d6ecea;
  }
  html, body {
    margin: 0;
    padding: 0;
    width: 1024px;
    height: 1200px;
    overflow: hidden;
    background: var(--backdrop);
  }
  .canvas {
    position: relative;
    width: 1024px;
    height: 1200px;
  }
  .card {
    position: absolute;
    background: var(--card);
    overflow: hidden;
  }
  /* Front side */
  .card-front {
    left: 29px; top: 33px; width: 574px; height: 325px;
  }
  .band {
    position: absolute; left: 0; width: 100%; height: 23px;
    background: var(--brand);
  }
  .band-top { top: 0; }
  .band-bottom { bottom: 0; }
  .mark-dot {
    position: absolute;
    border-radius: 50%;
    background: var(--brand);
  }
  .card-front .mark-dot {
    left: 78px; top: 104px; width: 118px; height: 118px;
  }
  .wordmark {
    position: absolute;
    margin: 0;
    font-family: "Open Sans", sans-serif;
    font-weight: 400;
    color: var(--text);
    line-height: 1;
    white-space: nowrap;
  }
  .card-front .wordmark {
    left: 208px; top: 133px; font-size: 55px; letter-spacing: -0.5px;
  }
  /* Back side */
  .card-back {
    left: 411px; top: 281px; width: 574px; height: 325px;
  }
  .backdrop-circle {
    position: absolute;
    left: 187px; top: 62px; width: 200px; height: 200px;
    border-radius: 50%;
    background: var(--brand-faint);
  }
  .divider {
    position: absolute;
    left: 286px; top: 80px; width: 1px; height: 165px;
    background: var(--rule);
  }
  .card-back .mark-dot {
    left: 20px; top: 129px; width: 69px; height: 69px;
  }
  .card-back .wordmark {
    left: 98px; top: 146px; font-size: 32px; letter-spacing: -0.3px;
  }
  .contact-list {
    position: absolute;
    left: 304px; top: 92px;
    margin: 0; padding: 0;
    list-style: none;
    font-family: "Lora", serif;
    font-size: 18px;
    color: var(--text);
  }
  .contact-item {
    display: flex;
    align-items: center;
    height: 40px;
  }
  .contact-icon {
    width: 20px; height: 20px;
    margin-right: 22px;
    fill: var(--brand);
    flex: none;
  }
</style>
</head>
<body>
<main class="canvas">

  <section class="card card-front" aria-label="Business card front">
    <div class="band band-top"></div>
    <div class="mark-dot"></div>
    <h1 class="wordmark">Veloristat</h1>
    <div class="band band-bottom"></div>
  </section>

  <section class="card card-back" aria-label="Business card back">
    <div class="backdrop-circle"></div>
    <div class="divider"></div>
    <div class="mark-dot"></div>
    <h2 class="wordmark">Veloristat</h2>
    <ul class="contact-list">
      <li class="contact-item">
        <svg class="contact-icon" viewBox="0 0 24 24" aria-hidden="true"><path d="M6.6 10.8c1.4 2.8 3.8 5.1 6.6 6.6l2.2-2.2c.3-.3.7-.4 1-.2 1.1.4 2.3.6 3.6.6.6 0 1 .4 1 1V20c0 .6-.4 1-1 1C10.6 21 3 13.4 3 4c0-.6.4-1 1-1h3.5c.6 0 1 .4 1 1 0 1.3.2 2.5.6 3.6.1.3 0 .7-.2 1L6.6 10.8z"/></svg>
        <span>1300 00 00 00</span>
      </li>
      <li class="contact-item">
        <svg class="contact-icon" viewBox="0 0 24 24" aria-hidden="true"><path d="M2 6.5C2 5.7 2.7 5 3.5 5h17c.8 0 1.5.7 1.5 1.5v.4l-10 6-10-6v-.4zM2 9.2l10 6 10-6v8.3c0 .8-.7 1.5-1.5 1.5h-17C2.7 19 2 18.3 2 17.5V9.2z"/></svg>
        <span>info@websitename.com</span>
      </li>
      <li class="contact-item">
        <svg class="contact-icon" viewBox="0 0 24 24" aria-hidden="true"><path d="M12 2c-3.9 0-7 3.1-7 7 0 5.2 7 13 7 13s7-7.8 7-13c0-3.9-3.1-7-7-7zm0 9.5a2.5 2.5 0 1 1 0-5 2.5 2.5 0 0 1 0 5z"/></svg>
        <span>Office Location</span>
      </li>
    </ul>
  </section>

</main>
</body>
</html>
```